Precise Finish Emulator (PFE)

I would like to design a dedicated site for my PFE product, which allows industry employees to be trained in the visual inspection of mechanical parts. My product is a 3D simulator (see https://norvik-works.ch/our-applications/virtual-reality/ and https://norvik-works.ch for videos) which makes it possible to manufacture standard parts representative of a type of defect which is accepted or refused by the quality department. These master parts can be used to create a common quality culture in the company and to train employees in a homogeneous way. The simulator is initially designed for watchmaking, but must be designed for much broader industries (cars, phone reconditioning, ball bearings, etc.)
L'information que j'ai donnée n'est pas assez précise. Je dois préciser les domaines métiers visés par le site internet. J'ai besoin de quelques jours pour choisir les domaines les plus représentatifs.

```html
<!DOCTYPE html>
<html lang="en">
<head>
<meta charset="utf-8">
<title>Precise Finish Emulator</title>
<link rel="stylesheet" href="https://fonts.googleapis.com/css2?family=Montserrat:wght@700;800&family=Questrial&family=Lato:wght@400&display=swap">
<style>
  :root {
    --header-bg: #f2f7fc;
    --navy: #15284a;
    --ink-dark: #1a1f2c;
    --brand-blue: #0b75bf;
    --white: #ffffff;
    --photo-light: #8a8a8a;
    --photo-dark: #2b2b2b;
  }
  * { margin: 0; padding: 0; box-sizing: border-box; }
  html, body { width: 1200px; height: 590px; overflow: hidden; background: var(--white); }
  .page { position: relative; width: 1200px; height: 590px; overflow: hidden; }

  .site-header {
    position: absolute; left: 0; top: 0; width: 1200px; height: 128px;
    background: var(--header-bg);
  }
  .brand { position: absolute; left: 74px; top: 28px; display: flex; align-items: center; gap: 18px; }
  .brand-mark { width: 62px; height: 62px; background: var(--navy); border-radius: 6px; }
  .brand-name {
    font-family: "Montserrat", sans-serif; font-weight: 700; font-size: 27px;
    color: var(--navy); letter-spacing: 0.5px;
  }
  .main-nav { position: absolute; top: 54px; left: 0; width: 100%; }
  .nav-link {
    position: absolute; font-family: "Montserrat", sans-serif; font-weight: 800;
    font-size: 16.5px; letter-spacing: 1.2px; color: var(--navy); text-decoration: none; white-space: nowrap;
  }
  .nav-link.is-active { color: var(--brand-blue); }
  .nav-home { left: 408px; }
  .nav-about { left: 524px; }
  .nav-services { left: 686px; }
  .nav-contact { left: 825px; }
  .cta-button {
    position: absolute; left: 1013px; top: 40px; width: 146px; height: 50px;
    border-radius: 25px; background: var(--brand-blue); color: var(--white);
    font-family: "Montserrat", sans-serif; font-weight: 800; font-size: 16.5px; letter-spacing: 1.2px;
    display: flex; align-items: center; justify-content: center; text-decoration: none;
  }

  .hero { position: absolute; left: 0; top: 128px; width: 1200px; height: 462px; }
  .hero-shapes { position: absolute; inset: 0; width: 1200px; height: 462px; display: block; }
  .hero-title {
    position: absolute; left: 46px; top: 204px;
    font-family: "Questrial", sans-serif; font-weight: 400; font-size: 44px; line-height: 44px;
    letter-spacing: 2.5px; color: var(--white);
  }
  .hero-tagline {
    position: absolute; left: 42px; top: 326px; width: 720px;
    font-family: "Lato", sans-serif; font-size: 20.5px; line-height: 32px;
    color: var(--white); text-transform: uppercase;
  }
</style>
</head>
<body>
<div class="page">
  <header class="site-header">
    <div class="brand">
      <span class="brand-mark"></span>
      <span class="brand-name">Norvik</span>
    </div>
    <nav class="main-nav">
      <a class="nav-link nav-home is-active" href="#">HOME</a>
      <a class="nav-link nav-about" href="#">ABOUT US</a>
      <a class="nav-link nav-services" href="#">SERVICES</a>
      <a class="nav-link nav-contact" href="#">CONTACT US</a>
    </nav>
    <a class="cta-button" href="#">TRY NOW</a>
  </header>

  <section class="hero">
    <svg class="hero-shapes" viewBox="0 0 1866 719" preserveAspectRatio="none">
      <defs>
        <linearGradient id="photo-tone" x1="0" y1="0" x2="1" y2="0.3">
          <stop offset="0" stop-color="var(--photo-dark)"/>
          <stop offset="0.45" stop-color="var(--photo-light)"/>
          <stop offset="1" stop-color="var(--photo-dark)"/>
        </linearGradient>
      </defs>
      <rect width="1866" height="719" fill="var(--ink-dark)"/>
      <polygon role="img" aria-label="Black and white photo of hands holding a small polished metal cube for visual inspection"
               points="1130,0 1866,0 1866,719 126,719" fill="url(#photo-tone)"/>
      <polygon points="1030,0 1125,0 985,135 890,135" fill="var(--brand-blue)"/>
      <polygon points="50,0 195,0 282,92 145,92" fill="var(--brand-blue)"/>
      <polygon points="213,0 355,0 375,20 375,163" fill="var(--white)"/>
      <polygon points="0,163 650,163 1225,719 0,719" fill="var(--brand-blue)"/>
    </svg>
    <h1 class="hero-title">Precise Finish<br>Emulator</h1>
    <p class="hero-tagline">Virtual reality at the service of controlled aesthetic<br>watchmaking</p>
  </section>
</div>
</body>
</html>
```